Louisiana personal injury attorney needs a postcard design

This will be the first of three post cards to go out to previous clients. We do not have intentions of making all three match/work with each other, but if you have an idea for that, please, let us know! This is for an attorney in Lafayette, LA that specializes in Medical Malpractice and Personal Injury. We would like the front of the post card to focus on those two practice areas and really grab someones attention!

the card in general will say: Glad to have served you, come see us for a free T-shirt, have a cup of coffee with us…

Please use a photo of the office for us to use on the back with a map of the office location (will send location when we pick the winner)

Industry/Entity Type

Legal

Font styles to use
Serif
Sans Serif

Requirements
Must have
• map of location of office. Large image or several images on the front. attention grabbing
Nice to have
• colors that match the logo. clean and easy to follow
Should not have
• should not be messy or too much going on.

```html
<!DOCTYPE html>
<html lang="en">
<head>
<meta charset="utf-8">
<title>Bellard Law Firm – Postcard</title>
<link rel="stylesheet" href="https://fonts.googleapis.com/css2?family=Open+Sans:wght@400;600;700&family=Aleo:wght@500;600&family=Oswald:wght@600&display=swap">
<style>
  :root {
    --navy: #174f8c;
    --gold: #c9992f;
    --gold-light: #dcae45;
    --ice: #dde9f0;
    --ink: #1d2228;
    --grey-text: #4f545a;
    --pill-dark: #3d3f42;
    --page: #e9e9ea;
    --white: #ffffff;
  }
  * { box-sizing: border-box; margin: 0; padding: 0; }
  html, body { width: 1200px; height: 2259px; overflow: hidden; }
  body {
    background: var(--page);
    font-family: "Open Sans", Arial, sans-serif;
    position: relative;
  }
  .postcard {
    position: absolute;
    left: 100px;
    width: 1000px;
    height: 665px;
    background: var(--white);
    overflow: hidden;
    box-shadow: 0 10px 30px rgba(0,0,0,.18);
  }
  .postcard--front { top: 424px; }
  .postcard--back { top: 1169px; }

  /* ---------- front ---------- */
  .brand-name {
    position: absolute;
    font-family: "Open Sans", Arial, sans-serif;
    font-weight: 700;
    color: var(--gold);
    text-align: center;
    line-height: 1;
    letter-spacing: 2px;
  }
  .front-brand { left: 0; width: 503px; top: 48px; font-size: 56px; }
  .front-brand small { display: block; font-size: 30px; letter-spacing: 10px; margin-top: 8px; }

  .moved-pill {
    position: absolute;
    left: 42px; top: 168px;
    width: 413px; height: 76px;
    border-radius: 40px;
    background: linear-gradient(#5a5c60, var(--pill-dark));
    border: 2px solid #9a9b9e;
    text-align: center;
    line-height: 1.15;
    padding-top: 8px;
    box-shadow: 0 4px 8px rgba(0,0,0,.3);
  }
  .moved-pill .headline { color: var(--gold-light); font-size: 25px; font-weight: 600; display: block; }
  .moved-pill .subline { color: var(--white); font-size: 25px; font-weight: 600; display: block; }

  .intro {
    position: absolute;
    left: 20px; width: 463px; top: 262px;
    text-align: center;
    font-size: 24px;
    line-height: 1.3;
    color: var(--grey-text);
  }
  .intro strong { color: var(--ink); font-weight: 700; }
  .intro .practice { color: var(--gold); font-weight: 600; }

  .consult-band {
    position: absolute;
    left: 0; top: 402px; width: 1000px; height: 146px;
    background: var(--navy);
  }
  .consult {
    position: absolute;
    left: 0; top: 406px; width: 503px;
    text-align: center;
    color: var(--white);
  }
  .consult .offer { font-size: 27px; font-weight: 600; line-height: 1.15; }
  .consult .offer span { display: inline-block; border-bottom: 2px solid var(--white); padding-bottom: 2px; }
  .phone-line {
    display: flex; align-items: center; justify-content: center; gap: 10px;
    font-family: "Oswald", Arial, sans-serif;
    font-weight: 600;
    font-size: 50px;
    line-height: 1.2;
  }
  .phone-line svg { width: 32px; height: 32px; }

  .name-band {
    position: absolute;
    left: 0; top: 548px; width: 1000px; height: 117px;
    background: var(--ice);
  }
  .name-notch {
    position: absolute;
    left: 240px; top: 548px;
    width: 0; height: 0;
    border-left: 12px solid transparent;
    border-right: 12px solid transparent;
    border-top: 12px solid var(--navy);
  }
  .firm-serif {
    position: absolute;
    left: 0; top: 562px; width: 503px;
    text-align: center;
    font-family: "Aleo", Georgia, serif;
    font-weight: 500;
    font-size: 46px;
    color: var(--ink);
  }
  .web-pill {
    position: absolute;
    left: 117px; top: 618px; width: 250px; height: 32px;
    border-radius: 16px;
    background: var(--gold);
    color: var(--white);
    font-family: "Aleo", Georgia, serif;
    font-size: 20px;
    text-align: center;
    line-height: 32px;
  }

  .office-photo {
    position: absolute;
    left: 503px; top: 37px; width: 497px; height: 456px;
    background: linear-gradient(180deg, #8fb2d8 0%, #cddcea 30%, #2d3447 55%, #3a3f52 70%, #5c8a3c 85%, #7aa84e 100%);
  }
  .interior-photo {
    position: absolute;
    top: 510px; height: 118px;
    border: 2px solid var(--white);
    box-shadow: 0 3px 6px rgba(0,0,0,.35);
  }
  .interior-photo--reception { left: 503px; width: 157px; background: linear-gradient(135deg, #e8e6e3, #9a8f86 60%, #6d4a3a); }
  .interior-photo--conference { left: 670px; width: 158px; background: linear-gradient(135deg, #5d6f80, #c9c2b6 55%, #7b5a45); }
  .interior-photo--boardroom { left: 838px; width: 162px; background: linear-gradient(135deg, #d9d5cf, #f0ede8 50%, #4a3a33); }

  /* ---------- back ---------- */
  .back-shapes { position: absolute; inset: 0; }
  .services-pill {
    position: absolute;
    left: 142px; top: 20px; width: 210px; height: 46px;
    border-radius: 23px;
    background: var(--gold);
    color: var(--white);
    font-family: "Aleo", Georgia, serif;
    font-weight: 500;
    font-size: 26px;
    text-align: center;
    line-height: 46px;
    box-shadow: 0 3px 6px rgba(0,0,0,.25);
  }
  .services {
    position: absolute;
    left: 48px; top: 104px;
    list-style: none;
    color: var(--white);
    font-size: 20px;
    line-height: 29px;
  }
  .services li { display: flex; align-items: center; gap: 14px; }
  .services svg { width: 17px; height: 17px; }

  .thanks {
    position: absolute;
    left: 50px; top: 298px; width: 400px;
    font-size: 20px;
    line-height: 1.27;
    font-weight: 600;
    color: var(--ink);
  }
  .location-map {
    position: absolute;
    left: 17px; top: 452px; width: 184px; height: 184px;
    border-radius: 50%;
    border: 4px solid var(--white);
    background: radial-gradient(circle at 45% 45%, #f4f4f2 0%, #e6e8e6 60%, #d7dcd8 100%);
  }
  .contact {
    position: absolute;
    left: 210px; top: 420px;
    color: var(--white);
  }
  .address { position: relative; padding-left: 30px; font-size: 19px; line-height: 1.3; }
  .address .label { font-weight: 600; color: var(--ink); }
  .address svg { position: absolute; left: 4px; top: 3px; width: 18px; height: 22px; }
  .contact .offer { margin-top: 28px; padding-left: 10px; font-size: 20px; font-weight: 700; line-height: 1.2; }
  .contact .offer span { display: inline-block; border-bottom: 2px solid var(--white); }
  .back-phone {
    display: flex; align-items: center; gap: 6px;
    padding-left: 8px;
    font-family: "Oswald", Arial, sans-serif;
    font-weight: 600;
    font-size: 34px;
    line-height: 1.3;
    color: var(--ink);
  }
  .back-phone svg { width: 22px; height: 22px; }
  .back-web { display: flex; align-items: center; gap: 8px; padding-left: 10px; font-size: 21px; font-weight: 600; color: var(--ink); }
  .back-web svg { width: 18px; height: 18px; }

  .back-brand { left: 585px; top: 62px; width: 230px; font-size: 44px; }
  .back-brand small { display: block; font-size: 24px; letter-spacing: 8px; margin-top: 6px; }
  .stamp-box {
    position: absolute;
    left: 851px; top: 34px; width: 114px; height: 113px;
    border: 2px solid var(--ink);
  }
  .address-line {
    position: absolute;
    left: 598px; width: 345px; height: 0;
    border-top: 2px solid #555;
  }
</style>
</head>
<body>

<section class="postcard postcard--front" aria-label="Postcard front">
  <div class="brand-name front-brand">BELLARD<small>LAW FIRM</small></div>

  <div class="moved-pill">
    <span class="headline">We Have Moved!</span>
    <span class="subline">Come See Our New Offices</span>
  </div>

  <p class="intro">Experienced Trial Attorneys in Lafayette, LA <strong>specializing</strong> in <span class="practice">Medical Malpractice</span> and <span class="practice">Personal Injury</span></p>

  <div class="consult-band"></div>
  <div class="consult">
    <div class="offer">GET A FREE<br><span>INITIAL CONSULTATION</span></div>
    <div class="phone-line">
      <svg viewBox="0 0 24 24" fill="currentColor"><path d="M6.6 10.8a15.1 15.1 0 0 0 6.6 6.6l2.2-2.2c.3-.3.7-.4 1-.2 1.1.4 2.3.6 3.6.6.6 0 1 .4 1 1V20c0 .6-.4 1-1 1A17 17 0 0 1 3 4c0-.6.4-1 1-1h3.5c.6 0 1 .4 1 1 0 1.3.2 2.5.6 3.6.1.3 0 .7-.2 1z"/></svg>
      337-555-0148
    </div>
  </div>

  <div class="name-band"></div>
  <div class="name-notch"></div>
  <div class="firm-serif">Bellard Law Firm</div>
  <div class="web-pill">www.bellardlaw.com</div>

  <div class="office-photo" role="img" aria-label="Photo of the new dark brick law office building with lawn and walkway"></div>
  <div class="interior-photo interior-photo--reception" role="img" aria-label="Photo of the office reception area"></div>
  <div class="interior-photo interior-photo--conference" role="img" aria-label="Photo of the conference room"></div>
  <div class="interior-photo interior-photo--boardroom" role="img" aria-label="Photo of the boardroom table"></div>
</section>

<section class="postcard postcard--back" aria-label="Postcard back">
  <svg class="back-shapes" viewBox="0 0 1000 665" width="1000" height="665">
    <rect x="0" y="0" width="1000" height="268" fill="var(--navy)"/>
    <rect x="0" y="268" width="1000" height="127" fill="var(--ice)"/>
    <rect x="0" y="395" width="1000" height="270" fill="var(--gold)"/>
    <path d="M640,0 Q262,332 640,665" fill="none" stroke="var(--white)" stroke-width="3"/>
    <path d="M628,0 Q250,332 628,665 L1000,665 L1000,0 Z" fill="var(--white)"/>
  </svg>

  <div class="services-pill">What We Do</div>
  <ul class="services">
    <li><svg viewBox="0 0 20 20" fill="none" stroke="#fff" stroke-width="2"><circle cx="10" cy="10" r="8"/><path d="M6 10l3 3 5-6"/></svg>Personal Injury</li>
    <li><svg viewBox="0 0 20 20" fill="none" stroke="#fff" stroke-width="2"><circle cx="10" cy="10" r="8"/><path d="M6 10l3 3 5-6"/></svg>Motor Vehicle Accidents</li>
    <li><svg viewBox="0 0 20 20" fill="none" stroke="#fff" stroke-width="2"><circle cx="10" cy="10" r="8"/><path d="M6 10l3 3 5-6"/></svg>Offshore Accident’s</li>
    <li><svg viewBox="0 0 20 20" fill="none" stroke="#fff" stroke-width="2"><circle cx="10" cy="10" r="8"/><path d="M6 10l3 3 5-6"/></svg>Catastrophic Injuries</li>
    <li><svg viewBox="0 0 20 20" fill="none" stroke="#fff" stroke-width="2"><circle cx="10" cy="10" r="8"/><path d="M6 10l3 3 5-6"/></svg>Medical Malpractice</li>
  </ul>

  <p class="thanks">We were glad to have served you.<br>Come see us for a free t-shirt and<br>a cup of coffee.</p>

  <div class="location-map" role="img" aria-label="Map showing the office location in Lafayette"></div>

  <div class="contact">
    <div class="address">
      <svg viewBox="0 0 18 22" fill="var(--ink)"><path d="M9 0a8 8 0 0 0-8 8c0 6 8 14 8 14s8-8 8-14a8 8 0 0 0-8-8zm0 11a3 3 0 1 1 0-6 3 3 0 0 1 0 6z"/></svg>
      <span class="label">Bellard Law Firm</span><br>
      220 Cypress Court<br>
      Lafayette, LA 70508
    </div>
    <div class="offer">GET A FREE<br><span>INITIAL CONSULTATION</span></div>
    <div class="back-phone">
      <svg viewBox="0 0 24 24" fill="currentColor"><path d="M6.6 10.8a15.1 15.1 0 0 0 6.6 6.6l2.2-2.2c.3-.3.7-.4 1-.2 1.1.4 2.3.6 3.6.6.6 0 1 .4 1 1V20c0 .6-.4 1-1 1A17 17 0 0 1 3 4c0-.6.4-1 1-1h3.5c.6 0 1 .4 1 1 0 1.3.2 2.5.6 3.6.1.3 0 .7-.2 1z"/></svg>
      337-555-0148
    </div>
    <div class="back-web">
      <svg viewBox="0 0 20 20" fill="none" stroke="var(--ink)" stroke-width="2"><circle cx="10" cy="10" r="8"/><path d="M2 10h16M10 2c3 3 3 13 0 16M10 2c-3 3-3 13 0 16"/></svg>
      www.bellardlaw.com
    </div>
  </div>

  <div class="brand-name back-brand">BELLARD<small>LAW FIRM</small></div>
  <div class="stamp-box"></div>
  <div class="address-line" style="top:357px"></div>
  <div class="address-line" style="top:420px"></div>
  <div class="address-line" style="top:486px"></div>
</section>

</body>
</html>
```